Collectible Fun Cards for Children

I have an idea of the type of card we want. Looking for an illustrator to help bring the idea to life very quickly. The cards will be in three series, with each series having a total of 36 cards each. I can supply most of the ideas for the cards but will need the successful designer to craft the cards in an attractive way. Ideally each car card will be of a different color. The preference will be for the two card images supplied to be merged. Of course, the successful candidate will be the one who is able to make come up with the best design, even better than the ones supplied.
I have added a hand-designed rendition of the card I have in mind for guidance.
The Purpose
• Engagement: Make kids excited to collect, trade, and read them.
• Education: Slip in simple but accurate nutrition, growth, and development facts.
• Branding: Position our brand as a premium, fun, and trustworthy product.

Target Market(s)

Children

Industry/Entity Type

Health and Wellness

Requirements
Must have
• Fun characters
Should not have
• Profanity. Incorrect information

```html
<!DOCTYPE html>
<html lang="en">
<head>
<meta charset="utf-8">
<title>NutriPals SuperSquad Hero Cards</title>
<link rel="stylesheet" href="https://fonts.googleapis.com/css2?family=Fredoka:wght@500;600&family=Nunito:ital,wght@1,800&display=swap">
<style>
  :root {
    --page-bg: #f7f7f7;
    --ink: #111111;
    --white: #ffffff;
  }
  * { box-sizing: border-box; margin: 0; padding: 0; }
  html, body { width: 849px; height: 1200px; overflow: hidden; background: var(--page-bg); }
  body { position: relative; font-family: "Fredoka", sans-serif; }

  .hero-card {
    position: absolute;
    width: 312px;
    height: 438px;
    background: var(--card-bg);
    overflow: hidden;
  }
  .hero-card--avocado { left: 89px; top: 117px; }
  .hero-card--honey { left: 445px; top: 119px; }
  .hero-card--strawberry { left: 90px; top: 592px; }
  .hero-card--meat { left: 445px; top: 592px; }

  .hero-card--avocado {
    --card-bg: #c4fb6d; --brand-bg: #c6fb6e; --brand-ink: #111;
    --title-bg: #236100; --label-bg: #236100; --label-ink: #fff;
    --value-bg: #f5d631; --value-ink: #1a1a1a;
    --pill-bg: #236100; --pill-ring: #f5d631; --num-bg: #fff; --num-ink: #236100;
    --art-a: #f4f7e9; --art-b: #7b5233; --art-ring: #f0b04a;
  }
  .hero-card--honey {
    --card-bg: #33223d; --brand-bg: #2e1f3b; --brand-ink: #fff;
    --title-bg: #dc6530; --label-bg: #dc6530; --label-ink: #fff;
    --value-bg: #fdcd36; --value-ink: #1a1a1a;
    --pill-bg: #dc6530; --pill-ring: #fdcd36; --num-bg: #fdcd36; --num-ink: #1a1a1a;
    --art-a: #ffffff; --art-b: #f5c32c; --art-ring: #f5c32c;
  }
  .hero-card--strawberry {
    --card-bg: #e81c2b; --brand-bg: #e81c2b; --brand-ink: #fff;
    --title-bg: #236100; --label-bg: #2ea600; --label-ink: #fff;
    --value-bg: #c8eafd; --value-ink: #1a1a1a;
    --pill-bg: #236100; --pill-ring: #8fd2f5; --num-bg: #c8eafd; --num-ink: #236100;
    --art-a: #ffffff; --art-b: #d91f2a; --art-ring: #5aaee8;
  }
  .hero-card--meat {
    --card-bg: #fdc9cb; --brand-bg: #eec0c0; --brand-ink: #111;
    --title-bg: #5f5f5f; --label-bg: #c0182e; --label-ink: #fff;
    --value-bg: #a2d7f3; --value-ink: #1a1a1a;
    --pill-bg: #e8317e; --pill-ring: #7a7a7a; --num-bg: #fff; --num-ink: #c0182e;
    --art-a: #ffffff; --art-b: #8a8a8a; --art-ring: #52b8ef;
  }

  .brand-strip {
    position: absolute; left: 0; top: 0; width: 100%; height: 35px;
    background: var(--brand-bg);
    color: var(--brand-ink);
    font-size: 16px; font-weight: 500;
    display: flex; align-items: center; justify-content: center;
  }
  .card-title {
    position: absolute; left: 0; top: 35px; width: 100%; height: 49px;
    background: var(--title-bg);
    color: var(--white);
    font-size: 22px; font-weight: 500; letter-spacing: 0.5px;
    display: flex; align-items: center; justify-content: center;
    box-shadow: 0 3px 6px rgba(0,0,0,0.25);
  }
  .hero-art {
    position: absolute; left: 50%; top: 100px;
    width: 168px; height: 168px; margin-left: -84px;
    border-radius: 50%;
    background: radial-gradient(circle at 50% 50%, var(--art-b) 0 42%, var(--art-a) 43% 100%);
    box-shadow: 0 0 0 3px var(--art-ring), 0 0 18px 4px var(--art-ring);
  }

  .hero-pill {
    position: absolute; left: 45px; top: 278px;
    width: 228px; height: 32px;
    border-radius: 16px;
    background: var(--pill-bg);
    border: 3px solid var(--pill-ring);
    color: var(--white);
    font-size: 16px; font-weight: 500;
    display: flex; align-items: center; padding-left: 15px;
  }
  .hero-pill__number {
    position: absolute; right: -3px; top: -3px;
    width: 32px; height: 32px; border-radius: 50%;
    background: var(--num-bg);
    border: 3px solid var(--pill-ring);
    color: var(--num-ink);
    font-size: 20px; font-weight: 600;
    display: flex; align-items: center; justify-content: center;
  }

  .stat-list {
    position: absolute; left: 0; top: 313px; width: 100%;
    display: flex; flex-direction: column; gap: 10px;
  }
  .stat-row {
    height: 20px;
    display: flex;
    font-size: 13px; font-weight: 500;
  }
  .stat-row__label {
    width: 124px; background: var(--label-bg); color: var(--label-ink);
    padding-left: 34px; display: flex; align-items: center;
  }
  .stat-row__value {
    flex: 1; margin-left: 12px; background: var(--value-bg); color: var(--value-ink);
    padding-left: 12px; display: flex; align-items: center; white-space: nowrap;
  }
  .hero-card--strawberry .stat-row__value { padding-left: 16px; }
  .hero-card--meat .stat-row__value { justify-content: center; padding-left: 0; }

  .series-caption {
    position: absolute; left: 0; top: 1075px; width: 100%;
    text-align: center;
    font-family: "Nunito", sans-serif; font-style: italic; font-weight: 800;
    font-size: 32px; color: var(--ink);
  }
</style>
</head>
<body>

<section class="hero-card hero-card--avocado">
  <div class="brand-strip">NutriPals</div>
  <h2 class="card-title">AVOCADO BEAR</h2>
  <div class="hero-art" role="img" aria-label="Illustration of a masked bear superhero in a green cape holding an avocado"></div>
  <div class="hero-pill">SUPERSQUAD HERO<span class="hero-pill__number">10</span></div>
  <div class="stat-list">
    <div class="stat-row"><span class="stat-row__label">Strength</span><span class="stat-row__value">Smart Thinking</span></div>
    <div class="stat-row"><span class="stat-row__label">Skill</span><span class="stat-row__value">Vitamin Unlock</span></div>
    <div class="stat-row"><span class="stat-row__label">Shield</span><span class="stat-row__value">Energy Density Shield</span></div>
    <div class="stat-row"><span class="stat-row__label">Source</span><span class="stat-row__value">Avocado,nuts,fish</span></div>
  </div>
</section>

<section class="hero-card hero-card--honey">
  <div class="brand-strip">NutriPals</div>
  <h2 class="card-title">HONEY BEE</h2>
  <div class="hero-art" role="img" aria-label="Illustration of a masked bee superhero holding a honey pot"></div>
  <div class="hero-pill">SUPERSQUAD HERO<span class="hero-pill__number">11</span></div>
  <div class="stat-list">
    <div class="stat-row"><span class="stat-row__label">Strength</span><span class="stat-row__value">Natural Healing</span></div>
    <div class="stat-row"><span class="stat-row__label">Skill</span><span class="stat-row__value">Energy Nectar</span></div>
    <div class="stat-row"><span class="stat-row__label">Shield</span><span class="stat-row__value">Golden Shield</span></div>
    <div class="stat-row"><span class="stat-row__label">Source</span><span class="stat-row__value">Honey</span></div>
  </div>
</section>

<section class="hero-card hero-card--strawberry">
  <div class="brand-strip">NutriPals</div>
  <h2 class="card-title">STRAWBERRY PANDA</h2>
  <div class="hero-art" role="img" aria-label="Illustration of a masked panda superhero in a red cape hugging a strawberry"></div>
  <div class="hero-pill">SUPERSQUAD HERO<span class="hero-pill__number">12</span></div>
  <div class="stat-list">
    <div class="stat-row"><span class="stat-row__label">Strength</span><span class="stat-row__value">Tummy Flow Rate</span></div>
    <div class="stat-row"><span class="stat-row__label">Skill</span><span class="stat-row__value">Sugar Control</span></div>
    <div class="stat-row"><span class="stat-row__label">Shield</span><span class="stat-row__value">Toxin Flush Shield</span></div>
    <div class="stat-row"><span class="stat-row__label">Source</span><span class="stat-row__value">Strawberry</span></div>
  </div>
</section>

<section class="hero-card hero-card--meat">
  <div class="brand-strip">NutriPals</div>
  <h2 class="card-title">MEAT DOG</h2>
  <div class="hero-art" role="img" aria-label="Illustration of a masked grey dog superhero in a pink cape holding a cut of meat"></div>
  <div class="hero-pill">SUPERSQUAD HERO<span class="hero-pill__number">13</span></div>
  <div class="stat-list">
    <div class="stat-row"><span class="stat-row__label">Strength</span><span class="stat-row__value">Blood Renewal</span></div>
    <div class="stat-row"><span class="stat-row__label">Skill</span><span class="stat-row__value">Oxygen Delivery</span></div>
    <div class="stat-row"><span class="stat-row__label">Shield</span><span class="stat-row__value">Stamina Shield</span></div>
    <div class="stat-row"><span class="stat-row__label">Source</span><span class="stat-row__value">Meat</span></div>
  </div>
</section>

<p class="series-caption">Animal superhero version</p>

</body>
</html>
```